Music Festival in Colorado Needs Awesome Flier Design

We need an eye-catching & captivating flier design for an annual music festival in Denver, CO (USA). The festival features the best Colorado musicians within the genres of jam - funk - bluegrass - electronic - reggae - rock.

The design should look clean and professional while still being creative and unique. The past three years' flier designs are attached, as well as the logo and some other designs that match the aesthetic of what we're looking for.

This festival has a big element of Colorado pride so any

Target Market(s)

Hippies - live music enthusiasts - partiers. Ages 21 - 40.

Industry/Entity Type

Entertainment

Colors
0355a3
ec1f27
ffffff
fbed22

Requirements
Must have
• Attached design text.
Nice to have
• - Quality texture and psychedelic elements.
• - Colorado pride elements; color scheme (red, white, blue & yellow), flag, ect.
• - Nature elements are awesome but this is also a downtown festival so keep that in mind.
Should not have
• Cheesy artwork.

```html
<!DOCTYPE html>
<html lang="en">
<head>
<meta charset="utf-8">
<title>Pass The Sound – Colorado Music Festival</title>
<link rel="stylesheet" href="https://fonts.googleapis.com/css2?family=Staatliches&display=swap">
<style>
  :root{
    --page:#ececec;
    --paper:#ffffff;
    --sky-top:#1670c0;
    --sky-mid:#2b6aa6;
    --sky-deep:#163f68;
    --logo:#c9d6e3;
    --ink:#ffffff;
    --snow:#e9edf2;
    --peak:#c6ccd5;
    --pine-blue:#2f5d86;
    --earth:#911c21;
    --earth-deep:#8a1a1f;
    --salmon:#e07a5f;
  }
  *{margin:0;padding:0;box-sizing:border-box;}
  html,body{width:1200px;height:1200px;overflow:hidden;}
  body{background:var(--page);font-family:"Staatliches",Impact,sans-serif;color:var(--ink);}
  .poster{position:absolute;left:190px;top:20px;width:820px;height:1160px;background:var(--paper);overflow:hidden;}
  .sky{position:absolute;left:0;top:12px;width:820px;height:700px;
    background:linear-gradient(180deg,var(--sky-top) 0%,var(--sky-mid) 40%,var(--sky-deep) 100%);}
  .scene{position:absolute;left:0;top:700px;width:820px;height:366px;
    background:linear-gradient(180deg,var(--peak) 0%,var(--snow) 24%,var(--pine-blue) 42%,var(--earth) 58%,var(--earth-deep) 100%);}
  .masthead{position:absolute;left:0;top:38px;width:820px;text-align:center;color:var(--logo);}
  .edition{font-size:20px;letter-spacing:2px;}
  .festival-name{line-height:.9;margin-top:4px;}
  .festival-name .small{display:block;font-size:34px;letter-spacing:1px;}
  .festival-name .big{display:block;font-size:104px;}
  .tagline{display:inline-block;margin-top:4px;font-size:12px;letter-spacing:2px;}
  .lineup{position:absolute;left:0;top:232px;width:820px;text-align:center;white-space:nowrap;}
  .lineup .headliners{font-size:34px;line-height:39px;letter-spacing:.5px;}
  .lineup .support{margin-top:4px;font-size:24px;line-height:27px;letter-spacing:.3px;}
  .details{position:absolute;left:70px;top:922px;}
  .dates{font-size:42px;line-height:46px;}
  .dates sup{font-size:22px;vertical-align:top;line-height:30px;}
  .venue{margin-top:4px;font-size:29px;line-height:32px;}
  .tickets{margin-top:6px;font-size:17px;}
  .tickets .label{color:var(--salmon);}
</style>
</head>
<body>
  <div class="poster">
    <div class="sky"></div>
    <div class="scene" role="img" aria-label="Illustrated snowy Colorado mountains with red and blue pine forest, a guitar, a microphone, a speaker and a vinyl record, and a winding path"></div>

    <header class="masthead">
      <div class="edition">6th Annual</div>
      <div class="festival-name"><span class="small">Pass The</span><span class="big">Sound</span></div>
      <div class="tagline">Colorado Music Festival</div>
    </header>

    <section class="lineup">
      <div class="headliners">Jeff Arden Band, Anyone Symphony,<br>Crack Theory, The Lucky Lentils,</div>
      <div class="support">
        B-Rock + The Summit, Gonefish Orchestra,<br>
        Tarmaka, Dinoseeker, Rapidwater Roam,<br>
        Prominence Ensemble, Vinyl Son, The Grove Ranch, Sun-<br>
        Dyed, Ivanhoff, Kinetics, Polyhorizon, Cable Depot,<br>
        Metasonics, Spectrum, Vivid Sight, Cable Depot,<br>
        Orbits, The Sweet Clovers, Zyeno Club, Jada Carver<br>
        Band, Atomix, Dubosaurus, Turtlex, Other Blue,<br>
        The Lazybones, Mama Marigold,<br>
        Ninth Ridge Brigade, Amorosa, Envy Ola,<br>
        Boogie Mastodon, Casual Captain, Mikey Lightning,<br>
        Wakonaset, Project 528, Summit Vibe, Kaleidoscape,<br>
        Casey Rowan + The Soul Shed, Lula Rising, Ninth<br>
        Ridge Brigade, Kilima.
      </div>
    </section>

    <section class="details">
      <div class="dates">May 11<sup>th</sup> – 13<sup>th</sup> 2018</div>
      <div class="venue">Lynx Street Yard<br>418 W. 52nd Ave Denver, CO 80221</div>
      <div class="tickets"><span class="label">Tickets + More Info :</span> www.passthesoundfest.com</div>
    </section>
  </div>
</body>
</html>
```